Professional modern business card design

A business card for my nutrition business, wanting a professional look, with info clearly visible. Open to using logo colours too.

Would like key info on the front -
logo
my name and qualifications
email
phone number

and just an enlarged logo again / image on the back.

```html
<!DOCTYPE html>
<html lang="en">
<head>
<meta charset="utf-8">
<title>RM Nutrition – Business Card</title>
<link rel="stylesheet" href="https://fonts.googleapis.com/css2?family=Montserrat:wght@400;500;700;800&display=swap">
<style>
  :root {
    --backdrop: #2e2926;
    --card: #ffffff;
    --navy: #10283d;
    --lime: #cad72c;
    --ink: #1d1d1d;
  }
  * { margin: 0; padding: 0; box-sizing: border-box; }
  html, body {
    width: 1200px; height: 786px; overflow: hidden;
    background: var(--backdrop);
    font-family: "Montserrat", Arial, sans-serif;
  }
  .stage {
    position: relative; width: 1200px; height: 786px;
    display: flex; align-items: center; justify-content: center; gap: 48px;
  }
  .card {
    position: relative; width: 520px; height: 336px;
    background: var(--card);
    overflow: hidden;
    box-shadow: 0 10px 30px rgba(0,0,0,.45);
  }
  .card-band {
    position: absolute; left: 0; right: 0; bottom: 0; height: 20px;
    background: var(--lime);
  }
  .wordmark {
    position: absolute; color: var(--navy); font-weight: 800;
    letter-spacing: .5px; white-space: nowrap; line-height: 1;
  }
  /* front */
  .card-front .wordmark { left: 40px; top: 58px; font-size: 46px; }
  .divider {
    position: absolute; left: 40px; right: 40px; top: 150px;
    height: 1px; background: var(--lime);
  }
  .contact-block { position: absolute; left: 40px; top: 196px; }
  .person-name { color: var(--lime); font-weight: 700; font-size: 19px; }
  .person-title { color: var(--ink); font-weight: 500; font-size: 12.5px; margin-top: 3px; }
  .title-rule { width: 250px; height: 1px; background: var(--lime); margin: 14px 0 14px; }
  .contact-row { display: flex; gap: 42px; font-size: 12.5px; color: var(--ink); }
  .contact-item { display: flex; align-items: center; gap: 8px; }
  .contact-item svg { width: 13px; height: 13px; fill: var(--lime); }
  /* back */
  .card-back .wordmark { left: 70px; top: 112px; font-size: 62px; }
</style>
</head>
<body>
<main class="stage">
  <section class="card card-front" aria-label="Card front">
    <div class="wordmark">RM Nutrition</div>
    <div class="divider"></div>
    <div class="contact-block">
      <p class="person-name">Rosalind Marsh</p>
      <p class="person-title">Specialist Rehabilitation Dietitian</p>
      <div class="title-rule"></div>
      <div class="contact-row">
        <span class="contact-item">
          <svg viewBox="0 0 24 24" aria-hidden="true"><path d="M6.6 10.8a15.2 15.2 0 0 0 6.6 6.6l2.2-2.2a1 1 0 0 1 1-.25 11.4 11.4 0 0 0 3.6.57 1 1 0 0 1 1 1V20a1 1 0 0 1-1 1A17 17 0 0 1 3 4a1 1 0 0 1 1-1h3.5a1 1 0 0 1 1 1c0 1.25.2 2.45.57 3.57a1 1 0 0 1-.25 1z"/></svg>
          07700900482
        </span>
        <span class="contact-item">
          <svg viewBox="0 0 24 24" aria-hidden="true"><path d="M2 5h20v14H2z M2 5l10 8 10-8" fill="none" stroke="#cad72c" stroke-width="2.4"/></svg>
          rosalind@rmnutrition.co.uk
        </span>
      </div>
    </div>
    <div class="card-band"></div>
  </section>

  <section class="card card-back" aria-label="Card back">
    <div class="wordmark">RM Nutrition</div>
    <div class="card-band"></div>
  </section>
</main>
</body>
</html>
```